HollowPine Ventures Inc. Business Card Design

My business is custom renovations and homes.I would need to have a new business logo created to go along with my company name. The business card should be of a modern style as this is the market I am focused on. I would need my contact information and website posted on the card. I would also like to list a few of the tasks I conduct on the card (such as: Renovations, Additions, Repairs, New Homes, Design, Consultations). On the reverse of the card I currently have just my logo and my motto, "Shaping A Bold Path". However, I am open to completely changing everything as I am starting a new year and would like to excel further. Any new ideas and suggestions are always welcomed. Thank you.

Target Market(s)

Upscale residential and commercial renovations and builds

Industry/Entity Type

Business

Contact Information for Business Card

I would like the design to be able to be laser cut or burnt onto a wooden business card. I will be creating one option of cards for really loyal customers (wooden) and a second option for the everyday customer (paper).

Font styles to use
Other font styles liked:
• Calibri / anything of mordern taste

Colors
f37122
5c5c5c
474747
ffffff

Requirements
Must have
• I would like the colours of my business to be a sharp orange and grey. I believe this will symbolize a modern style. I am open to other suggestions if this is not suitable for the designers tastes. My contact info as follows:
• Will Marsh
• President
• HollowPine Ventures Inc.
• 555-214-3987
• will@hollowpineventures.example
• I would like my website (currently under construction) hollowpineventures.example on the card aswell.
Nice to have
• Along with a modern logo representing HollowPine, I would like something on the card besides the logo and contact information. Perhaps a small background design. I feel it may be nice to have my services listed on the card (in smaller font on the bottom) Renovations, Additions, Repairs, Design, Consultations.
Should not have
• The business card should not have too many different colors. Should not have rounded corners.

```html
<!DOCTYPE html>
<html lang="en">
<head>
<meta charset="utf-8">
<title>HollowPine Ventures Inc. – Business Card</title>
<link rel="stylesheet" href="https://fonts.googleapis.com/css2?family=Carlito:wght@400;700&family=Open+Sans:wght@400&family=Ubuntu:wght@500;700&display=swap">
<style>
  :root {
    --stage-blue: #00aeef;
    --brand-orange: #f37122;
    --brand-amber: #fbab24;
    --charcoal: #474747;
    --slate: #5c5c5c;
    --ink: #1e1e1e;
    --paper: #ffffff;
  }
  html, body {
    margin: 0;
    padding: 0;
    overflow: hidden;
  }
  .canvas {
    position: relative;
    width: 1200px;
    height: 1200px;
    background: var(--stage-blue);
    overflow: hidden;
  }
  .card {
    position: absolute;
    left: 230px;
    display: block;
  }
  .card--front { top: 110px; width: 742px; height: 423px; }
  .card--back  { top: 645px; width: 745px; height: 424px; }

  .brand-name {
    font-family: "Carlito", "Calibri", sans-serif;
    font-weight: 700;
    fill: var(--brand-orange);
  }
  .contact-text {
    font-family: "Open Sans", sans-serif;
    font-size: 24px;
    fill: var(--charcoal);
    letter-spacing: 0.5px;
  }
  .company-mark {
    font-family: "Carlito", "Calibri", sans-serif;
    font-size: 54px;
    fill: var(--ink);
  }
  .company-legal {
    font-family: "Open Sans", sans-serif;
    font-size: 28px;
    fill: var(--ink);
  }
  .person-name {
    font-family: "Ubuntu", sans-serif;
    font-weight: 700;
    font-size: 54px;
    fill: var(--paper);
  }
  .person-title {
    font-family: "Ubuntu", sans-serif;
    font-weight: 700;
    font-size: 26px;
    fill: var(--paper);
  }
  .services {
    font-family: "Carlito", "Calibri", sans-serif;
    font-size: 31px;
    fill: var(--ink);
  }
  .services .divider { fill: var(--brand-orange); font-weight: 700; }
  .icon-box { fill: var(--charcoal); stroke: var(--slate); stroke-width: 3; }
  .icon-glyph { fill: none; stroke: var(--paper); stroke-width: 2.5; stroke-linecap: round; stroke-linejoin: round; }
  .rule { stroke: var(--brand-orange); stroke-width: 2.5; }
</style>
</head>
<body>
<main class="canvas">

  <!-- Front of card -->
  <svg class="card card--front" viewBox="0 0 928 529" aria-label="Business card front">
    <rect width="928" height="529" fill="var(--charcoal)"/>
    <g class="edge-stripe edge-stripe--top">
      <rect x="0" y="0" width="928" height="21" fill="var(--brand-orange)"/>
      <polygon points="218,0 420,0 398,21 196,21" fill="var(--brand-amber)"/>
      <polygon points="420,0 622,0 600,21 398,21" fill="var(--paper)"/>
    </g>
    <g class="edge-stripe edge-stripe--bottom">
      <rect x="0" y="508" width="928" height="21" fill="var(--brand-orange)"/>
      <polygon points="322,508 524,508 502,529 300,529" fill="var(--paper)"/>
      <polygon points="524,508 730,508 708,529 502,529" fill="var(--brand-amber)"/>
    </g>
    <text class="brand-name" x="464" y="300" font-size="118" text-anchor="middle">HollowPine</text>
  </svg>

  <!-- Back of card -->
  <svg class="card card--back" viewBox="0 0 931 530" aria-label="Business card back">
    <rect width="931" height="530" fill="var(--paper)"/>
    <polygon class="panel-dark" points="0,0 212,0 400,344 0,344" fill="var(--charcoal)"/>
    <polygon class="panel-slash" points="212,0 268,0 455,344 400,344" fill="var(--brand-orange)"/>
    <rect x="0" y="343" width="928" height="4" fill="var(--brand-orange)"/>

    <text class="brand-name" x="150" y="245" font-size="56" text-anchor="middle">HollowPine</text>

    <!-- Contact details -->
    <g class="contact contact--phone">
      <text class="contact-text" x="820" y="86" text-anchor="end">555-214-3987</text>
      <rect class="icon-box" x="853" y="49" width="48" height="48"/>
      <path class="icon-glyph" d="M866 62 l5 -3 l5 8 l-4 3 q3 7 10 10 l3 -4 l8 5 l-3 5 q-14 0 -24 -24 z"/>
    </g>
    <line class="rule" x1="466" y1="119" x2="902" y2="119"/>
    <g class="contact contact--email">
      <text class="contact-text" x="826" y="184" text-anchor="end">will@hollowpineventures.example</text>
      <rect class="icon-box" x="853" y="149" width="48" height="48"/>
      <rect class="icon-glyph" x="863" y="162" width="28" height="20"/>
      <path class="icon-glyph" d="M863 162 l14 11 l14 -11 M863 182 l10 -9 M891 182 l-10 -9"/>
    </g>
    <line class="rule" x1="466" y1="219" x2="902" y2="219"/>
    <g class="contact contact--web">
      <text class="contact-text" x="824" y="277" text-anchor="end">hollowpineventures.example</text>
      <rect class="icon-box" x="853" y="249" width="48" height="48"/>
      <circle class="icon-glyph" cx="877" cy="273" r="15"/>
      <path class="icon-glyph" d="M862 273 h30 M877 258 q-9 15 0 30 M877 258 q9 15 0 30"/>
    </g>

    <!-- Identity band -->
    <text class="company-mark" x="38" y="403">HollowPine</text>
    <text class="company-legal" x="38" y="431">HollowPine Ventures Inc.</text>
    <polygon points="408,354 460,354 515,452 463,452" fill="var(--slate)"/>
    <polygon points="460,354 928,354 928,452 515,452" fill="var(--brand-orange)"/>
    <text class="person-name" x="556" y="408">Will Marsh</text>
    <text class="person-title" x="569" y="442">President</text>
    <rect x="0" y="459" width="928" height="3" fill="var(--brand-orange)"/>

    <!-- Services -->
    <text class="services" x="464" y="507" text-anchor="middle">Renovations<tspan class="divider"> | </tspan>Additions<tspan class="divider"> | </tspan>Repairs<tspan class="divider">|</tspan>Design<tspan class="divider">|</tspan>Consultations.</text>
  </svg>

</main>
</body>
</html>
```